Flyer für Zeitarbeitsfirma
Zielgruppe
Wir sind eine Zeitarbeitsfirma in der Pflege! Unsere Kunden sind Krankenhäuser und Pflegeheime
Aufgabenstellung
Wir möchten eine Art Flyer als erste Seite einer Bewerbungsmappe.
Überschrift: Bewerbung als Personaldienstleister
Warum K7-CURAVIT?
Wir bieten entscheidende Unterschiede:
1 Tag KOSTENFREI
(Vermindern Sie Ihr Risiko für schlechtes Zeitarbeitspersonal)
5 Tage günstiger Einarbeitungstarif
anschließend erhalten Sie eine Preisgarantie fürs gesamte Jahr
PLUS kostenfreie Übernahme unserer Mitarbeiter
Worauf warten Sie noch?
Wir freuen uns auf eine tolle Zusammenarbeit!
www.kobalt-7.de

```html
<!DOCTYPE html>
<html lang="de">
<head>
<meta charset="utf-8">
<title>Bewerbung als Personaldienstleister – K7-CURAVIT</title>
<link href="https://fonts.googleapis.com/css2?family=Fira+Sans:wght@400;600;700&family=Merriweather:ital,wght@0,400;0,700;0,900;1,400&display=swap" rel="stylesheet">
<style>
:root{
  --stage:#c4c4c4;
  --paper:#ffffff;
  --red:#d2503c;
  --green:#1e9a4a;
  --ink:#4a4a4a;
  --slate:#5b5b5b;
  --rule:#555;
}
*{box-sizing:border-box;margin:0;padding:0}
html,body{width:1200px;height:897px;overflow:hidden}
body{background:var(--stage);position:relative;font-family:"Merriweather",Georgia,serif;color:var(--ink)}
.spread{position:absolute;width:630px;height:430px;display:grid;grid-template-columns:repeat(3,1fr);background:var(--paper);box-shadow:0 4px 14px rgba(0,0,0,.25)}
.spread--outside{left:24px;top:14px}
.spread--inside{left:546px;top:452px}
.panel{position:relative;height:430px;border-right:1px solid #e4e4e4;overflow:hidden}
.panel:last-child{border-right:none}

/* outside: contact panel */
.contact{display:flex;flex-direction:column}
.contact__text{padding:22px 16px 0 18px;height:232px;font-family:"Fira Sans",Arial,sans-serif}
.contact__title{color:var(--red);font-weight:700;font-size:12.5px;line-height:1.2;text-transform:uppercase}
.contact__lead{color:var(--red);font-weight:600;font-size:8.6px;line-height:1.55;margin-top:4px}
.contact__block{margin-top:16px;padding-left:18px;font-size:6.8px;line-height:1.75;color:#555}
.contact__block strong{display:block;font-size:6.8px;color:#333;font-weight:700}
.contact__row{display:flex;align-items:center;gap:4px;margin-left:-12px}
.contact__row svg{width:8px;height:8px;fill:#2d6b4a}
.photo{flex:1}
.photo--caller{background:linear-gradient(160deg,#b59a84,#6e5a4c 55%,#2f5b50)}

/* outside: benefits panel */
.benefits{padding:18px 14px}
.benefits__frame{border:1px solid var(--rule);height:100%;padding:12px 12px}
.benefits__title{color:var(--green);font-weight:900;font-size:11.5px;line-height:1.15;text-transform:uppercase}
.benefits__title .initial{font-size:26px;float:left;line-height:.9;margin-right:2px}
.benefits__intro{font-style:italic;font-size:11px;line-height:1.2;color:#444;margin:18px 0 18px 8px}
.benefits__intro .initial{font-size:26px;float:left;line-height:.85;margin-right:2px;font-style:normal;font-weight:700}
.benefit{color:var(--red);font-size:7.6px;line-height:1.35;margin:0 0 14px 8px}
.benefit svg{display:block;width:14px;height:18px;margin-bottom:3px}

/* cover panel */
.cover{display:flex;flex-direction:column}
.cover__head{padding:24px 14px 0;text-align:center;height:150px}
.cover__kicker{color:var(--red);font-weight:700;font-size:15px;line-height:1.2;text-transform:uppercase;text-align:left;padding-left:30px}
.brand{display:inline-flex;align-items:center;gap:4px;font-weight:700;font-size:9px;color:var(--green);margin:2px 0 0 70px}
.brand__dot{width:10px;height:10px;border-radius:50%;background:var(--green)}
.cover__title{color:var(--red);font-weight:700;font-size:15px;line-height:1.25;text-transform:uppercase;margin-top:12px}
.photo--care{flex:1;background:linear-gradient(135deg,#e9dcd1,#c9b4a4 45%,#8a7566)}
.cover__foot{height:38px;display:flex;align-items:center;padding-left:36px;color:var(--green);font-weight:700;font-size:8px;text-transform:uppercase}

/* inside: dark panel */
.offer{background:var(--slate);color:#fff;padding:16px 12px}
.offer__title{color:var(--green);font-weight:700;font-size:9px;text-transform:uppercase;text-align:center;line-height:1.2}
.offer__free{color:var(--red);font-weight:700;font-size:8.4px;margin-top:8px;line-height:1.25}
.offer__free small{display:block;font-size:7.4px;font-weight:400}
.offer__rate{font-weight:700;font-size:9.4px;line-height:1.15;margin:8px 0 4px 24px}
.offer__list{list-style:none;font-size:6.2px;font-weight:700;line-height:1.3;margin-left:24px}
.photo--visit{height:150px;margin:8px 0 0 0;background:linear-gradient(120deg,#c8c6c0,#b56c5c 45%,#7f8fb2)}
.offer__ask{font-weight:700;font-size:12.5px;line-height:1.15;margin-top:10px}
.offer__thanks{color:var(--red);font-weight:700;font-size:12px;line-height:1.2;margin:12px 0 0 28px}

/* inside: text panels */
.story{padding:34px 16px 14px;font-size:7.4px;line-height:1.5;color:#555}
.story__headline{position:absolute;top:14px;left:222px;width:420px;color:var(--red);font-weight:900;font-size:23px;letter-spacing:.5px;text-transform:uppercase;white-space:nowrap}
.story h3{font-size:8.4px;font-weight:900;color:#333;text-transform:uppercase;line-height:1.2;margin:8px 0 5px}
.story p+h3{margin-top:22px}
.photo--round{float:right;width:92px;height:92px;border-radius:50%;margin:90px -8px 4px 6px;shape-outside:circle(50%);background:linear-gradient(140deg,#f2ede2,#c9b89c 45%,#2d4f9a)}
</style>
</head>
<body>

<section class="spread spread--outside" aria-label="Außenseite">
  <div class="panel contact">
    <div class="contact__text">
      <h2 class="contact__title">Fordern Sie Ihr individuelles Angebot an</h2>
      <p class="contact__lead">Arbeiten Sie bei uns – in Ihrer Region! Kennenlern- und Vorstellungsgespräche finden immer in Ihrer Nähe statt. Wir kommen zu Ihnen!</p>
      <div class="contact__block">
        <strong>KONTAKTIEREN SIE UNS!</strong>
        Kobalt 7 Personalservice GmbH<br>
        Lindenallee 14<br>
        79098 Freiburg
        <div class="contact__row"><svg viewBox="0 0 10 10"><path d="M2 1l2 2-1 1.2c.6 1.2 1.6 2.2 2.8 2.8L7 6l2 2-1.4 1.4C4.5 9 1 5.5.6 2.4z"/></svg>TEL 0761 555 203 0</div>
        <div class="contact__row"><svg viewBox="0 0 10 10"><path d="M0 2h10v6H0zM1 3l4 3 4-3"/></svg>MAIL info@kobalt-7.de</div>
        <div class="contact__row"><svg viewBox="0 0 10 10"><circle cx="5" cy="5" r="4.5"/></svg>WEB www.kobalt-7.de</div>
      </div>
    </div>
    <div class="photo photo--caller" role="img" aria-label="Foto: junge Frau telefoniert lächelnd am Tisch"></div>
  </div>

  <div class="panel benefits">
    <div class="benefits__frame">
      <h2 class="benefits__title"><span class="initial">M</span>ehr Sicherheit &amp; Wertschätzung für Pflegefachkräfte</h2>
      <p class="benefits__intro"><span class="initial">G</span>estalten Sie sich eine Karriere, die sich Ihrem Leben anpasst, nicht umgekehrt. Gemeinsam mit uns kreieren Sie sich:</p>
      <p class="benefit"><svg viewBox="0 0 14 18"><path d="M1 10l4 7L13 1" fill="none" stroke="#d2503c" stroke-width="2"/></svg>Mehr Geld bei spürbar weniger Arbeitsbelastung</p>
      <p class="benefit"><svg viewBox="0 0 14 18"><path d="M1 10l4 7L13 1" fill="none" stroke="#d2503c" stroke-width="2"/></svg>Mehr Sicherheit durch komplett abgesicherten Arbeitsvertrag</p>
      <p class="benefit"><svg viewBox="0 0 14 18"><path d="M1 10l4 7L13 1" fill="none" stroke="#d2503c" stroke-width="2"/></svg>Mehr Freiheit durch räumlich &amp; zeitlich attraktive Arbeitsmodelle</p>
    </div>
  </div>

  <div class="panel cover">
    <div class="cover__head">
      <p class="cover__kicker">Bewerbung<br>&nbsp;&nbsp;&nbsp;als</p>
      <span class="brand"><span class="brand__dot"></span>K7-CURAVIT</span>
      <h1 class="cover__title">Personal-<br>dienstleister</h1>
    </div>
    <div class="photo photo--care" role="img" aria-label="Foto: Pflegerin legt einer älteren Dame lächelnd die Hand auf die Schulter"></div>
    <p class="cover__foot">Warum K7-CURAVIT?</p>
  </div>
</section>

<section class="spread spread--inside" aria-label="Innenseite">
  <div class="panel offer">
    <h2 class="offer__title">Wir bieten entscheidende Unterschiede:</h2>
    <p class="offer__free">1 Tag KOSTENFREI<small>(Vermindern Sie Ihr Risiko für schlechtes Zeitarbeitspersonal)</small></p>
    <p class="offer__rate">5 Tage günstiger Einarbeitungstarif</p>
    <ul class="offer__list">
      <li>• anschließend erhalten Sie eine Preisgarantie fürs gesamte Jahr</li>
      <li>• PLUS kostenfreie Übernahme unserer Mitarbeiter</li>
    </ul>
    <div class="photo photo--visit" role="img" aria-label="Foto: Pflegerin im Gespräch mit einer Seniorin im Rollstuhl"></div>
    <p class="offer__ask">Worauf warten<br>Sie noch?</p>
    <p class="offer__thanks">Wir freuen uns auf eine tolle Zusammenarbeit!</p>
  </div>

  <div class="panel story">
    <h3>Ehrlich. Transparent. Persönlich.</h3>
    <p>Wie oft haben Sie schon „Werte“ in Werbeslogans gelesen und festgestellt, dass diese meist nur leere Worte waren? Vor allem in der Jobvermittlung und Zeitarbeit sind die Erfahrungen, die Fachkräfte machen müssen, häufig mit mehr Enttäuschungen verbunden, als der Joballtag bereits für Sie parat hält. Da kommt schnell die Frage auf: Wann hat diese Suche nach dem idealen Job bloß ein Ende?</p>
    <h3>Ergebnisse unseres außergewöhnlichen Konzepts</h3>
    <p>So durften hunderte Fachkräfte dank unserer Modelle das Gefühl der Erfüllung, dass Sie noch zu Beginn Ihres Berufs hatten, zurückerlangen. Sie sehnen sich ebenfalls nach dem Gefühl zurück, welches nur ein sozialer Job mit sich bringt? Dann erleben Sie diese Freude erneut in Ihrer wertvollen Tätigkeit, indem Sie sich bei uns bewerben. Gemeinsam meistern wir das!</p>
  </div>

  <div class="panel story">
    <h3>Morgens, mittags oder abends? Auf zum Neubeginn!</h3>
    <div class="photo--round" role="img" aria-label="Foto: Pflegerin in blauer Kleidung bei der Arbeit"></div>
    <p>Sollten Sie nun schmunzeln, bitten wir Sie diesen Ausdruck der Freude weiter auszuweiten, denn unser Team aus Experten ist darauf spezialisiert, die Version Ihres Wunschjobs im Bereich Pflege Wirklichkeit werden zu lassen. Wann? Genau dann, wenn Sie es möchten! Dabei liegt unser einzigartiges Erfolgskonzept darin, dass wir Ihren Bedürfnissen die größte Aufmerksamkeit schenken. Deshalb bauen wir auch Arbeitsmodelle komplett auf Ihren Vorstellungen auf. Mehr Urlaub, mehr Geld, mehr Mobilität? Beinahe alles ist möglich und die Zufriedenheit unserer betreuten Fachkräfte hat dies mehrfach bewiesen.</p>
  </div>
  <h2 class="story__headline">Wir für Sie!</h2>
</section>

</body>
</html>
```